Hospital Digital Whiteboard UI/UX Redesign

We are looking to update the look and feel of our Digital Whiteboards.
There are 4 separate layouts: Patient TV, Patient Room Whiteboard, Digital Door Sign, and Unit Care Board.
We want to have a unified, modern look across the portfolio.

```html
<!DOCTYPE html>
<html lang="en">
<head>
<meta charset="utf-8">
<title>Clearwell Health – Digital Whiteboard Suite</title>
<link rel="stylesheet" href="https://fonts.googleapis.com/css2?family=Poppins:wght@400;500;600;700;800&display=swap">
<style>
  :root {
    --stage: #c8e3f0;
    --panel: #eceef3;
    --shade: rgba(160, 172, 192, 0.55);
    --light: #ffffff;
    --ink: #1b1b1f;
    --navy: #1a1f8c;
    --sky: #2ab0ea;
    --bar: #2e6fb0;
    --green: #5ab94a;
    --code-green: #2e7d32;
    --red: #d3302a;
    --orange: #ef7d00;
    --yellow: #e6b800;
    --teal: #22a396;
    --steel: #2a6490;
  }
  * { box-sizing: border-box; margin: 0; padding: 0; }
  html, body { width: 1200px; height: 1135px; overflow: hidden; }
  body {
    background: var(--stage);
    font-family: "Poppins", sans-serif;
    color: var(--ink);
    position: relative;
  }
  .screen {
    position: absolute;
    background: var(--panel);
    box-shadow: 0 4px 14px rgba(90, 120, 150, 0.18);
  }
  .raised {
    position: absolute;
    background: var(--panel);
    border-radius: 9px;
    box-shadow: 4px 4px 8px var(--shade), -3px -3px 7px var(--light);
  }
  .center { display: flex; flex-direction: column; align-items: center; justify-content: center; text-align: center; }
  .brand-word { font-weight: 500; color: var(--green); letter-spacing: 0.2px; }

  /* Patient TV */
  .tv { left: 57px; top: 116px; width: 534px; height: 385px; }
  .tv-header {
    position: absolute; left: 0; top: 0; width: 100%; height: 46px;
    box-shadow: 0 3px 5px rgba(160, 172, 192, 0.45);
  }
  .tv-header .brand-word { position: absolute; left: 36px; top: 15px; font-size: 11px; }
  .tv-title { position: absolute; left: 0; width: 100%; top: 15px; text-align: center; font-size: 10px; font-weight: 600; }
  .tv-clock { position: absolute; left: 420px; width: 60px; top: 13px; text-align: center; font-size: 13px; }
  .menu-btn { width: 72px; height: 54px; }
  .menu-btn .bar { position: absolute; left: 11px; top: 12px; width: 50px; height: 5px; border-radius: 3px; background: var(--bar); }
  .menu-btn .label { position: absolute; left: 0; width: 100%; top: 28px; text-align: center; font-size: 9.5px; }
  .video-card { left: 135px; top: 64px; width: 265px; height: 258px; border-radius: 12px; }
  .video-frame {
    position: absolute; left: 6px; top: 7px; width: 253px; height: 246px; border-radius: 10px;
    background: linear-gradient(150deg, #e8e4de 0%, #c9c2b8 45%, #8a6a4c 100%);
    overflow: hidden;
  }
  .video-title { position: absolute; left: 9px; top: 10px; font-size: 10px; font-weight: 600; }
  .play { position: absolute; left: 102px; top: 98px; }
  .tagline { position: absolute; left: 0; width: 100%; top: 341px; text-align: center; font-size: 20px; font-weight: 600; color: var(--navy); }

  /* Shared room pieces */
  .room-label { font-size: 13px; color: var(--navy); line-height: 1; }
  .room-number { font-size: 52px; font-weight: 700; color: var(--sky); line-height: 1; letter-spacing: -1px; margin-top: 4px; }
  .action { font-size: 13.5px; font-weight: 600; color: var(--green); }
  .action .brand-word { font-size: 12px; }

  /* Door sign */
  .door { left: 619px; top: 135px; width: 536px; height: 366px; }
  .quote { font-size: 23px; line-height: 1.5; }
  .quote-by { font-size: 12px; color: var(--navy); margin-top: 4px; }

  /* Whiteboards */
  .board { top: 555px; width: 535px; height: 464px; }
  .board.alert { left: 55px; }
  .board.care { left: 619px; }
  .tag { left: 106px; width: 46px; height: 44px; align-items: flex-start; padding-left: 10px; }
  .tag b { font-size: 15px; font-weight: 700; line-height: 1; }
  .tag span { font-size: 7px; margin-top: 2px; }
  .code-text { font-size: 58px; font-weight: 800; line-height: 0.95; color: var(--code-green); letter-spacing: -0.5px; }
  .timer { position: absolute; left: 30px; top: 137px; width: 205px; height: 49px; border-radius: 25px; font-size: 20px; }
  .elapsed { position: absolute; left: 0; width: 100%; top: 205px; text-align: center; font-size: 14px; color: var(--navy); }
  .visitors { font-size: 14px; color: var(--navy); line-height: 1.5; }
  .avatar {
    position: absolute; left: 10px; top: 8px; width: 46px; height: 46px; border-radius: 50%;
    background: radial-gradient(circle at 50% 40%, #b8875e 0%, #7d5a43 55%, #cfd5dc 100%);
    box-shadow: 2px 2px 5px var(--shade), -2px -2px 4px var(--light);
  }
  .person-name { position: absolute; left: 75px; top: 18px; font-size: 10px; font-weight: 600; }
  .person-role { position: absolute; left: 75px; top: 37px; font-size: 5.5px; }
  .note { position: absolute; left: 30px; width: 205px; height: 32px; border-radius: 16px; }
  .note b { position: absolute; left: 20px; top: 3px; font-size: 13px; font-weight: 700; }
  .note .sub { position: absolute; left: 20px; top: 21px; font-size: 5.5px; }
  .note .detail { position: absolute; left: 129px; top: 21px; font-size: 5.5px; }
</style>
</head>
<body>

<!-- Patient TV -->
<section class="screen tv">
  <header class="tv-header">
    <span class="brand-word">Clearwell</span>
    <p class="tv-title">Welcome to clearwell health</p>
    <p class="tv-clock">02 : 24</p>
  </header>

  <div class="raised menu-btn" style="left:50px;top:65px"><i class="bar"></i><p class="label">My Care</p></div>
  <div class="raised menu-btn" style="left:50px;top:132px"><i class="bar"></i><p class="label">EDUCATION</p></div>
  <div class="raised menu-btn" style="left:50px;top:200px"><i class="bar"></i><p class="label">Rearxh</p></div>
  <div class="raised menu-btn" style="left:50px;top:267px"><i class="bar"></i><p class="label">My Care</p></div>

  <div class="raised video-card">
    <div class="video-frame" role="img" aria-label="Welcome video still: team meeting around a white table in a bright office">
      <p class="video-title">Welcome Video</p>
      <svg class="play" width="50" height="50" viewBox="0 0 50 50" aria-hidden="true">
        <circle cx="25" cy="25" r="25" fill="#2e6fb0"/>
        <path d="M16 21 L34 15 L27 33 L25 24 Z" fill="#fff"/>
      </svg>
    </div>
  </div>

  <div class="raised menu-btn" style="left:413px;top:65px"><i class="bar"></i><p class="label">RX Search</p></div>
  <div class="raised menu-btn" style="left:413px;top:132px"><i class="bar"></i><p class="label">Watch Tv</p></div>
  <div class="raised menu-btn" style="left:413px;top:200px"><i class="bar"></i><p class="label">Movies</p></div>
  <div class="raised menu-btn" style="left:413px;top:267px"><i class="bar"></i><p class="label">Audio</p></div>

  <p class="tagline">Making each day matter</p>
</section>

<!-- Digital door sign -->
<section class="screen door">
  <div class="raised center" style="left:142px;top:27px;width:279px;height:88px">
    <p class="room-label">ROOM</p>
    <p class="room-number">216</p>
  </div>
  <div class="raised center" style="left:142px;top:127px;width:279px;height:144px">
    <p class="quote">“Believe you can<br>you are<br>halfway there.”</p>
    <p class="quote-by">-Eleanor Whitby</p>
  </div>
  <div class="raised center action" style="left:142px;top:287px;width:83px;height:60px">Admin</div>
  <div class="raised center action" style="left:241px;top:287px;width:83px;height:60px"><span class="brand-word">Clearwell</span></div>
  <div class="raised center action" style="left:338px;top:287px;width:83px;height:60px">Floor Map</div>
</section>

<!-- Unit care board: alert state -->
<section class="screen board alert">
  <div class="raised center tag" style="top:30px"><b style="color:var(--red)">CP</b><span>Lorem</span></div>
  <div class="raised center tag" style="top:82px"><b style="color:var(--red)">DP</b><span>Lorem</span></div>
  <div class="raised center tag" style="top:134px"><b style="color:var(--orange)">LA</b><span>Lorem</span></div>
  <div class="raised center tag" style="top:186px"><b style="color:var(--yellow)">FR</b><span>Lorem</span></div>
  <div class="raised center tag" style="top:238px"><b style="color:var(--code-green)">EN</b><span>Lorem</span></div>
  <div class="raised center tag" style="top:290px"><b style="color:var(--teal)">NS</b><span>Lorem</span></div>
  <div class="raised center tag" style="top:342px"><b style="color:var(--teal)">NS</b><span>Lorem</span></div>
  <div class="raised center tag" style="top:394px"><b style="color:var(--steel)">VE</b><span>Lorem</span></div>

  <div class="raised center" style="left:164px;top:29px;width:265px;height:84px">
    <p class="room-label">ROOM</p>
    <p class="room-number">216</p>
  </div>
  <div class="raised" style="left:164px;top:125px;width:265px;height:240px">
    <p class="code-text" style="position:absolute;left:0;width:100%;top:14px;text-align:center">CODE<br>BLUE</p>
    <div class="raised center timer">02 : 24</div>
    <p class="elapsed">Elapsed Time</p>
  </div>
  <div class="raised center action" style="left:164px;top:378px;width:79px;height:57px">Admin</div>
  <div class="raised center action" style="left:257px;top:378px;width:79px;height:57px"><span class="brand-word">Clearwell</span></div>
  <div class="raised center action" style="left:350px;top:378px;width:79px;height:57px">Floor Map</div>
</section>

<!-- Patient room whiteboard -->
<section class="screen board care">
  <div class="raised center tag" style="top:30px"><b style="color:var(--red)">CP</b><span>Lorem</span></div>
  <div class="raised center tag" style="top:82px"><b style="color:var(--red)">DP</b><span>Lorem</span></div>
  <div class="raised center tag" style="top:134px"><b style="color:var(--orange)">LA</b><span>Lorem</span></div>
  <div class="raised center tag" style="top:186px"><b style="color:var(--yellow)">FR</b><span>Lorem</span></div>
  <div class="raised center tag" style="top:238px"><b style="color:var(--code-green)">EN</b><span>Lorem</span></div>
  <div class="raised center tag" style="top:290px"><b style="color:var(--teal)">NS</b><span>Lorem</span></div>
  <div class="raised center tag" style="top:342px"><b style="color:var(--teal)">NS</b><span>Lorem</span></div>
  <div class="raised center tag" style="top:394px"><b style="color:var(--steel)">VE</b><span>Lorem</span></div>

  <div class="raised center" style="left:164px;top:29px;width:265px;height:84px">
    <p class="room-label">ROOM</p>
    <p class="room-number">216</p>
  </div>
  <div class="raised center" style="left:164px;top:125px;width:265px;height:63px">
    <p class="visitors">VISITORS<br>WELCOME</p>
  </div>
  <div class="raised" style="left:164px;top:201px;width:265px;height:62px">
    <div class="avatar" role="img" aria-label="Portrait photo of the care team lead"></div>
    <p class="person-name">Jordan Ellis</p>
    <p class="person-role">CEO - Clearwell Health</p>
  </div>
  <div class="raised" style="left:164px;top:276px;width:265px;height:89px">
    <div class="raised note" style="top:9px"><b>WATER</b><span class="sub">Lorem</span><span class="detail">Lorem ipsum dummy</span></div>
    <div class="raised note" style="top:48px"><b>BED HEIGHT</b><span class="sub">Lorem</span><span class="detail">Lorem ipsum dummy</span></div>
  </div>
  <div class="raised center action" style="left:164px;top:378px;width:79px;height:57px">Admin</div>
  <div class="raised center action" style="left:257px;top:378px;width:79px;height:57px"><span class="brand-word">Clearwell</span></div>
  <div class="raised center action" style="left:350px;top:378px;width:79px;height:57px">Floor Map</div>
</section>

</body>
</html>
```